Carpentry and Building Business Card

I'm looking for a business card that is minimalistic and that incorporates the theme of my Velmor logo.
On one side I'd like the VELMOR logo with my details on the other side.
Double sided with curved edges

Target Market(s)

Construction / renovation
Adults

Industry/Entity Type

Tradesman

Contact Information for Business Card

Logo on one side, details on the other

Colors

Designer to choose only greyscale colors for use in the design.

Requirements
Must have
• Nilo Petrakis
VELMOR CONSTRUCT
Carpentry & Building Services
0481236574
Velmorconstruct@brixmail.com
Lic No. 718263D
Nice to have
• Fb and insta icons. @velmorconstruct
Should not have
• No hammer or tool icons please.

No address line.

```html
<!DOCTYPE html>
<html lang="en">
<head>
<meta charset="utf-8">
<title>Velmor Construct – Business Card</title>
<link rel="stylesheet" href="https://fonts.googleapis.com/css2?family=Montserrat:wght@400;700&display=swap">
<style>
  :root {
    --page-bg: #e4e4e2;
    --card-bg: #3a3a3b;
    --card-edge: #2c2c2d;
    --ink: #ffffff;
    --ink-soft: #e0e0e0;
    --ink-muted: #b5b5b5;
    --accent: #bdbdbd;
  }
  * { box-sizing: border-box; margin: 0; padding: 0; }
  html, body {
    width: 1200px; height: 892px; overflow: hidden;
    background: var(--page-bg);
    font-family: "Montserrat", Arial, sans-serif;
  }
  .sheet {
    position: relative; width: 1200px; height: 892px;
    display: flex; flex-direction: column; align-items: center; justify-content: center; gap: 40px;
  }
  .card {
    position: relative; width: 620px; height: 379px;
    background: var(--card-bg);
    border-radius: 16px;
    box-shadow: 0 2px 0 var(--card-edge), 0 10px 24px rgba(0,0,0,.18);
    color: var(--ink);
  }
  /* Front */
  .card--front { display: flex; align-items: center; justify-content: center; }
  .brand { display: flex; align-items: center; gap: 26px; }
  .brand__mark {
    width: 58px; height: 58px;
    border: 3px solid var(--accent);
  }
  .brand__name {
    font-weight: 400; font-size: 50px; letter-spacing: 16px;
    color: var(--ink);
  }
  /* Back */
  .details { position: absolute; left: 58px; top: 56px; }
  .details__name {
    font-weight: 700; font-size: 27px; line-height: 1.2; letter-spacing: .5px; text-transform: uppercase;
  }
  .details__company {
    font-weight: 400; font-size: 21px; line-height: 1.2; margin-top: 2px; text-transform: uppercase; color: var(--ink-soft);
  }
  .details__services {
    font-weight: 400; font-size: 14px; line-height: 1.2; margin-top: 6px; color: var(--ink-muted);
  }
  .contact { list-style: none; margin-top: 18px; }
  .contact__item {
    display: flex; align-items: center; gap: 12px;
    font-size: 15px; line-height: 1; color: var(--ink-soft); margin-bottom: 9px;
  }
  .contact__icon { width: 16px; height: 16px; flex: none; }
  .brand--small { position: absolute; right: 46px; bottom: 40px; gap: 14px; }
  .brand--small .brand__mark { width: 34px; height: 34px; border-width: 2px; }
  .brand--small .brand__name { font-size: 28px; letter-spacing: 8px; }
</style>
</head>
<body>
<main class="sheet">
  <section class="card card--front" aria-label="Card front">
    <div class="brand">
      <span class="brand__mark"></span>
      <span class="brand__name">VELMOR.</span>
    </div>
  </section>

  <section class="card card--back" aria-label="Card back">
    <div class="details">
      <h1 class="details__name">Nilo Petrakis</h1>
      <p class="details__company">VELMOR CONSTRUCT</p>
      <p class="details__services">Carpentry &amp; Building Services</p>
      <ul class="contact">
        <li class="contact__item">
          <svg class="contact__icon" viewBox="0 0 16 16"><circle cx="8" cy="8" r="7.2" fill="none" stroke="var(--accent)" stroke-width="1.3"/><path d="M5.6 4.4l1.3 1.3-.7 1.1c.6 1.3 1.5 2.2 2.8 2.8l1.1-.7 1.3 1.3-.9 1.1C8 11.2 4.8 8 4.5 5.3z" fill="var(--accent)"/></svg>
          <span>0481236574</span>
        </li>
        <li class="contact__item">
          <svg class="contact__icon" viewBox="0 0 16 16"><circle cx="8" cy="8" r="8" fill="var(--accent)"/><rect x="4" y="5.2" width="8" height="5.6" fill="none" stroke="var(--card-bg)" stroke-width="1"/><path d="M4 5.4l4 3 4-3" fill="none" stroke="var(--card-bg)" stroke-width="1"/></svg>
          <span>Velmorconstruct@brixmail.com</span>
        </li>
        <li class="contact__item">
          <svg class="contact__icon" viewBox="0 0 16 16"><circle cx="8" cy="8" r="8" fill="var(--accent)"/><path d="M4.5 6.5h7M4.5 9.5h7" stroke="var(--card-bg)" stroke-width="1.3"/></svg>
          <span>Lic No. 718263D</span>
        </li>
        <li class="contact__item">
          <svg class="contact__icon" viewBox="0 0 16 16"><circle cx="8" cy="8" r="8" fill="var(--accent)"/></svg>
          <span>@velmorconstruct</span>
        </li>
      </ul>
    </div>
    <div class="brand brand--small">
      <span class="brand__mark"></span>
      <span class="brand__name">VELMOR.</span>
    </div>
  </section>
</main>
</body>
</html>
```